Business Card Design for a Sound engineer and DJ

We would like a residn of the business card.

Logo must remain the same.
The card is for the owner of the company.
The business card is in Arabic as the company is based in Kuwait.
The company specializes in sound engineering for singers concerts and events and in addition DJ.
The color options is up to the designer but we would like it masculine as the owner is a man.

Target Market(s)

All ages

Industry/Entity Type

Media

Contact Information for Business Card

Name:
Eng. Faisal Barrak
م/فيصل براك

The name above is in Arabic and English.

Title: General Manager
Mobile: +965 96370482
Office: +965 22480637
Email: info@qamarwave.net

Address:
Office no. 3
1st floor
Marjan Complex
Hamad Faraj St.
Salmiya
Kuwait

Instagram: @qamarwave
Snap: qamarwave

Requirements
Nice to have
• can we have Instagram icon and snap icon and a phone vector and email?
• Instead of writing the words

```html
<!DOCTYPE html>
<html lang="en">
<head>
<meta charset="utf-8">
<title>Qamar Wave – Business Card</title>
<link href="https://fonts.googleapis.com/css2?family=Josefin+Sans:wght@300;400;600&family=Tajawal:wght@300;400;500&display=swap" rel="stylesheet">
<style>
  :root {
    --stage: #d9d9dc;
    --card: #050505;
    --purple: #5d4fae;
    --band-blue: #5a6cc4;
    --lavender: #b9b2ec;
    --violet: #8e7fe0;
    --pink: #c8449a;
    --cyan: #63c9e3;
    --rule: #5466d8;
    --text: #d9d9e3;
  }
  * { box-sizing: border-box; margin: 0; padding: 0; }
  html, body { width: 1200px; height: 926px; overflow: hidden; }
  body {
    background: var(--stage);
    font-family: "Josefin Sans", sans-serif;
    display: flex;
    flex-direction: column;
    align-items: center;
    justify-content: center;
    gap: 40px;
  }
  .card {
    position: relative;
    width: 720px;
    height: 400px;
    background: var(--card);
    overflow: hidden;
    box-shadow: 0 10px 28px rgba(0,0,0,.25);
  }

  /* Shared brand lockup */
  .brand__name {
    display: flex; align-items: center; justify-content: center; gap: 14px;
    color: var(--lavender); font-weight: 400; font-size: 46px; letter-spacing: 8px;
    white-space: nowrap;
  }
  .brand__dot { width: 16px; height: 16px; border-radius: 50%; background: var(--violet); flex: none; }
  .brand__tagline { margin-top: 14px; color: var(--violet); font-size: 17px; letter-spacing: 3px; white-space: nowrap; }
  .brand__tagline-ar { margin-top: 6px; color: var(--violet); font-family: "Tajawal", sans-serif; font-size: 19px; white-space: nowrap; }

  /* Front */
  .tab { position: absolute; width: 34px; height: 62px; background: var(--purple); }
  .tab--left { left: 0; top: 62px; }
  .tab--right { right: 0; bottom: 120px; }
  .brand-main {
    position: absolute; left: 0; right: 0; top: 130px;
    display: flex; flex-direction: column; align-items: center;
  }

  /* Back */
  .band-top { position: absolute; top: 0; left: 0; right: 0; height: 10px; background: var(--purple); }
  .band-bottom { position: absolute; bottom: 0; left: 0; right: 0; height: 18px; background: var(--band-blue); }
  .person { position: absolute; left: 46px; top: 48px; width: 340px; }
  .person__name-ar { font-family: "Tajawal", sans-serif; font-weight: 300; color: var(--violet); font-size: 30px; direction: rtl; text-align: left; }
  .person__name { margin-top: 8px; color: var(--lavender); font-size: 21px; letter-spacing: 2px; white-space: nowrap; }
  .person__title { color: var(--pink); font-size: 15px; letter-spacing: 2.5px; white-space: nowrap; }
  .person__rule { margin-top: 10px; height: 1px; background: var(--rule); }
  .contacts { list-style: none; margin-top: 14px; }
  .contacts li { display: flex; align-items: center; gap: 10px; color: var(--text); font-size: 17px; font-weight: 300; line-height: 26px; white-space: nowrap; }
  .contacts svg { width: 15px; height: 15px; flex: none; }

  .brand-mini {
    position: absolute; right: 40px; top: 96px; width: 270px;
    display: flex; flex-direction: column; align-items: center;
  }
  .brand-mini .brand__name { font-size: 28px; letter-spacing: 5px; gap: 10px; }
  .brand-mini .brand__dot { width: 11px; height: 11px; }
  .brand-mini .brand__tagline { font-size: 11px; letter-spacing: 2px; margin-top: 8px; }
  .brand-mini .brand__tagline-ar { font-size: 13px; margin-top: 3px; }

  .divider { position: absolute; left: 46px; right: 44px; top: 262px; height: 1px; background: var(--rule); }
  .social { position: absolute; right: 60px; top: 274px; list-style: none; width: 170px; }
  .social li { display: flex; align-items: center; gap: 10px; color: var(--text); font-size: 18px; font-weight: 400; line-height: 26px; }
  .social__mark { width: 15px; height: 15px; border-radius: 50%; background: var(--cyan); flex: none; }
  .address { position: absolute; left: 46px; bottom: 38px; color: var(--text); font-size: 14.5px; font-weight: 300; white-space: nowrap; }
</style>
</head>
<body>

  <section class="card card--front" aria-label="Card front">
    <div class="tab tab--left"></div>
    <div class="tab tab--right"></div>
    <div class="brand-main">
      <div class="brand__name"><span class="brand__dot"></span>QAMAR WAVE</div>
      <div class="brand__tagline">DJ - SOUND ENG. - LIGHTING</div>
      <div class="brand__tagline-ar" dir="rtl">دي جي - هندسة صوت - إضاءة</div>
    </div>
  </section>

  <section class="card card--back" aria-label="Card back">
    <div class="band-top"></div>

    <div class="person">
      <p class="person__name-ar" dir="rtl">م/فيصل براك</p>
      <p class="person__name">ENG. FAISAL BARRAK</p>
      <p class="person__title">GENERAL MANAGER</p>
      <div class="person__rule"></div>
      <ul class="contacts">
        <li>
          <svg viewBox="0 0 16 16"><rect x="4" y="1" width="8" height="14" rx="1.5" fill="none" stroke="var(--cyan)" stroke-width="1.5"/><circle cx="8" cy="12.5" r="0.9" fill="var(--cyan)"/></svg>
          +965 96370482
        </li>
        <li>
          <svg viewBox="0 0 16 16"><rect x="4" y="1" width="8" height="14" rx="1.5" fill="none" stroke="var(--cyan)" stroke-width="1.5"/><circle cx="8" cy="12.5" r="0.9" fill="var(--cyan)"/></svg>
          +965 22480637 (office)
        </li>
        <li>
          <svg viewBox="0 0 16 16"><rect x="1" y="3" width="14" height="10" fill="var(--cyan)"/><path d="M1 3 L8 9 L15 3" fill="none" stroke="var(--card)" stroke-width="1.2"/></svg>
          info@qamarwave.net
        </li>
      </ul>
    </div>

    <div class="brand-mini">
      <div class="brand__name"><span class="brand__dot"></span>QAMAR WAVE</div>
      <div class="brand__tagline">DJ - SOUND ENG. - LIGHTING</div>
      <div class="brand__tagline-ar" dir="rtl">دي جي - هندسة صوت - إضاءة</div>
    </div>

    <div class="divider"></div>
    <ul class="social">
      <li><span class="social__mark"></span>@qamarwave</li>
      <li><span class="social__mark"></span>qamarwave</li>
    </ul>

    <p class="address">Office no. 3, 1st floor, Marjan Complex, Hamad Faraj St., Salmiya, Kuwait</p>
    <div class="band-bottom"></div>
  </section>

</body>
</html>
```